The Verdant Ledger App - Modernization & Graphics User Interface Friendliness Updates

We are Verdant Ledger, and we want to bring a new branding look and graphical user interface to the Verdant Ledger App. The app is a quick reference encyclopedia for all things produce. Boasting articles on over 2,000 produce items, with information ranging from taste and application to geographical and cultural significance. Included in its features are over 10 thousand recipes, and the Verdant Ledger App Harvest Circle – a global initiative to connect farmer, customer, and chef in one sustainable and easy to use application. The design needs to bring a greater sense of social connection – encouraging the user to participate in the 'Harvest Circled' experience voluntarily. The design should reflect a sense of authority reflecting the authenticity and reliability of the provided information, it's writing, and its sources. Download the App here: vledgr.example/install

Target Market(s)

Women and Men between ages 21-55.

Industry/Entity Type

Education

Font styles to use
Serif
Sans Serif

Colors

Designer to choose colors to be used in the design.

Requirements
Must have
• An updated user interface, the intuitive usability of the app is currently non-existent. We are looking to reflect as the authority on produce. The app design must reflect a professional, user-friendly, up-to-date, and trustworthy feel.
Nice to have
• To incorporate the social draw of the Harvest Circle we would like to include on the home page "Social Bubbles" (think Pictoloop stories) which updates with shared photos of produce and their location.
Should not have
• An overly complicated theme, distracting or unprofessional colors, and images.

```html
<!DOCTYPE html>
<html lang="en">
<head>
<meta charset="utf-8">
<title>Verdant Ledger – Categories</title>
<link rel="stylesheet" href="https://fonts.googleapis.com/css2?family=Roboto:wght@400;500;700&display=swap">
<style>
  :root {
    --stage: #1f1f1f;
    --screen: #ffffff;
    --ink: #1a1a1a;
    --muted: #555555;
    --green: #0f9a1d;
    --green-dark: #0b8a17;
    --rule: #d6d6d6;
    --tile-border: #cfcfcf;
    --badge: #e8334a;
  }
  * { box-sizing: border-box; margin: 0; padding: 0; }
  html, body { width: 1200px; height: 857px; overflow: hidden; }
  body {
    background: var(--stage);
    font-family: "Roboto", sans-serif;
    color: var(--ink);
    position: relative;
  }
  .screen {
    position: absolute;
    left: 370px; top: 20px;
    width: 400px; height: 710px;
    transform: scale(1.15);
    transform-origin: top left;
    background: var(--screen);
    overflow: hidden;
  }
  .status-bar {
    position: absolute; left: 0; top: 0; width: 100%; height: 22px;
    font-size: 11px; display: flex; align-items: center; justify-content: space-between;
    padding: 0 10px;
  }
  .status-bar .time { position: absolute; left: 0; right: 0; text-align: center; }
  .signal { display: flex; gap: 2px; align-items: center; }
  .signal span { width: 5px; height: 5px; border-radius: 50%; background: var(--ink); }
  .battery { display: flex; align-items: center; gap: 4px; }
  .header {
    position: absolute; top: 30px; left: 0; width: 100%; height: 38px;
    border-bottom: 1px solid var(--rule);
  }
  .header .title {
    position: absolute; left: 0; right: 0; top: 6px; text-align: center;
    color: var(--green); font-weight: 700; font-size: 20px;
  }
  .header svg { position: absolute; }
  .grid { position: absolute; top: 80px; left: 12px; width: 376px; }
  .tile { position: absolute; width: 116px; }
  .tile .photo { width: 116px; height: 116px; border: 1px solid var(--tile-border); }
  .tile .label {
    text-align: center; font-size: 13px; line-height: 15px; margin-top: 9px; letter-spacing: .2px;
  }
  .produce-button {
    position: absolute; left: 136px; top: 77px; width: 128px; height: 36px;
    background: var(--green); color: #fff; border-radius: 5px;
    font-size: 15px; display: flex; align-items: center; padding-left: 23px;
  }
  .produce-button svg { position: absolute; right: 6px; top: 5px; }
  .tab-bar {
    position: absolute; left: 0; bottom: 0; width: 100%; height: 56px;
    border-top: 1px solid var(--rule); background: var(--screen);
  }
  .tab { position: absolute; top: 6px; width: 60px; text-align: center; font-size: 10px; color: var(--muted); }
  .tab svg { display: block; margin: 0 auto 3px; }
  .tab.active { color: var(--green); }
  .badge {
    position: absolute; top: -1px; min-width: 18px; height: 13px; border-radius: 7px;
    background: var(--badge); color: #fff; font-size: 10px; line-height: 13px; padding: 0 3px;
  }
</style>
</head>
<body>
<main class="screen">
  <div class="status-bar">
    <div class="signal"><span></span><span></span><span></span><span></span><span></span>
      <svg width="12" height="9" viewBox="0 0 12 9"><path d="M6 8.5 L1 3.5 A7 7 0 0 1 11 3.5 Z" fill="#1a1a1a"/></svg></div>
    <div class="time">11:47</div>
    <div class="battery">86%
      <svg width="24" height="10" viewBox="0 0 24 10"><rect x=".5" y=".5" width="21" height="9" rx="1.5" fill="none" stroke="#1a1a1a"/><rect x="2" y="2" width="16" height="6" fill="#1a1a1a"/><rect x="22" y="3" width="1.5" height="4" fill="#1a1a1a"/></svg></div>
  </div>

  <header class="header">
    <svg style="left:16px;top:7px" width="24" height="24" viewBox="0 0 24 24"><circle cx="10" cy="10" r="8" fill="none" stroke="var(--green)" stroke-width="1.5"/><line x1="16" y1="16" x2="22" y2="22" stroke="var(--green)" stroke-width="1.5"/></svg>
    <h1 class="title">Categories</h1>
    <svg style="left:315px;top:11px" width="24" height="18" viewBox="0 0 24 18" stroke="var(--green)" stroke-width="1"><line x1="0" y1="2" x2="2" y2="2"/><line x1="5" y1="2" x2="24" y2="2"/><line x1="0" y1="7" x2="2" y2="7"/><line x1="5" y1="7" x2="24" y2="7"/><line x1="0" y1="12" x2="2" y2="12"/><line x1="5" y1="12" x2="24" y2="12"/><line x1="0" y1="17" x2="2" y2="17"/><line x1="5" y1="17" x2="24" y2="17"/></svg>
    <svg style="left:363px;top:12px" width="18" height="18" viewBox="0 0 18 18" fill="none" stroke="var(--green)" stroke-width="1"><rect x=".5" y=".5" width="7" height="7"/><rect x="10.5" y=".5" width="7" height="7"/><rect x=".5" y="10.5" width="7" height="7"/><rect x="10.5" y="10.5" width="7" height="7"/></svg>
  </header>

  <section class="grid">
    <div class="tile" style="left:0;top:0"><div class="photo" role="img" aria-label="Assorted fruit: grapes, pineapple, starfruit, apple and kiwi" style="background:linear-gradient(135deg,#3a2a4a,#b8862c 45%,#8fb04a 65%,#c9302a)"></div><p class="label">All Fruit</p></div>
    <div class="tile" style="left:130px;top:0"><div class="photo" role="img" aria-label="Red tomatoes on the vine" style="background:linear-gradient(160deg,#6f9a3a,#cf2b14 55%,#8cae4c)"></div><p class="label">All Vegetable</p></div>
    <div class="tile" style="left:259px;top:0"><div class="photo" role="img" aria-label="Plated world specialty dish with greens and sauce" style="background:linear-gradient(150deg,#7a3a1c,#c77a2a 50%,#e9e2d6)"></div><p class="label">World Specialty</p></div>

    <div class="tile" style="left:0;top:158px"><div class="photo" role="img" aria-label="Bunch of dried lavender" style="background:linear-gradient(140deg,#8a7ab4,#4f4676 50%,#a99bd0)"></div><p class="label">Edible Flower</p></div>
    <div class="tile" style="left:130px;top:158px"><div class="photo" role="img" aria-label="Fresh mint leaves" style="background:radial-gradient(circle at 50% 50%,#6cae4c,#3f8a2f 60%,#e9f1e4)"></div><p class="label">Herbs</p></div>
    <div class="tile" style="left:259px;top:158px"><div class="photo" role="img" aria-label="Green artichoke-like bud" style="background:linear-gradient(170deg,#6e6a5a,#4f7a34 45%,#2d3a1f)"></div><p class="label" style="margin-top:4px">Interesting and Unusual</p></div>

    <div class="tile" style="left:0;top:314px"><div class="photo" role="img" aria-label="Bunch of green leaves" style="background:linear-gradient(150deg,#f2f2f2,#3f7a2e 40%,#2c5c22 80%,#f2f2f2)"></div><p class="label">Leaves</p></div>
    <div class="tile" style="left:130px;top:314px"><div class="photo" role="img" aria-label="White oyster mushrooms" style="background:radial-gradient(circle at 45% 50%,#efe8da,#d9cfbd 55%,#fafafa)"></div><p class="label">Mushrooms</p></div>
    <div class="tile" style="left:259px;top:314px"><div class="photo" role="img" aria-label="Ginger root" style="background:linear-gradient(150deg,#fafafa,#c9a56a 40%,#a07a3f 70%,#e9d86a)"></div><p class="label">Root</p></div>

    <div class="tile" style="left:0;top:466px"><div class="photo" role="img" aria-label="Sunflower in bloom" style="background:radial-gradient(circle at 50% 60%,#5a3a16 20%,#f1cf1a 45%,#9fb8d8)"></div></div>
    <div class="tile" style="left:130px;top:466px"><div class="photo" role="img" aria-label="Cut brown-skinned root with white flesh" style="background:linear-gradient(180deg,#6a3416,#9b5a2e 45%,#f0ede6)"></div></div>
    <div class="tile" style="left:259px;top:466px"><div class="photo" role="img" aria-label="Bundle of long green leafy stalks" style="background:linear-gradient(170deg,#f2f2f2,#4f8a3a 40%,#2f6a24)"></div></div>
  </section>

  <div class="produce-button">All Produce
    <svg width="14" height="26" viewBox="0 0 14 26"><path d="M2 2 L12 13 L2 24" fill="none" stroke="#fff" stroke-width="1.5"/></svg>
  </div>

  <nav class="tab-bar">
    <div class="tab" style="left:12px">
      <svg width="28" height="28" viewBox="0 0 28 28"><path d="M3 13 L14 3 L25 13 L22 13 L22 26 L16 26 L16 18 L12 18 L12 26 L6 26 L6 13 Z" fill="#5a5a5a"/></svg>Home</div>
    <div class="tab active" style="left:86px">
      <svg width="28" height="28" viewBox="0 0 28 28" fill="var(--green)"><rect x="2" y="2" width="7" height="7"/><rect x="11" y="2" width="7" height="7"/><rect x="20" y="2" width="7" height="7"/><rect x="2" y="11" width="7" height="7"/><rect x="11" y="11" width="7" height="7"/><rect x="20" y="11" width="7" height="7"/><rect x="2" y="20" width="7" height="7"/><rect x="11" y="20" width="7" height="7"/><rect x="20" y="20" width="7" height="7"/></svg>Category</div>
    <div class="tab" style="left:170px">
      <svg width="28" height="28" viewBox="0 0 28 28" fill="none" stroke="#5a5a5a" stroke-width="1.5"><circle cx="14" cy="16" r="9"/><path d="M14 11 L14 16 L18 18"/><path d="M5 4 L7 6 M3 8 L6 8"/></svg>Updated
      <span class="badge" style="left:34px">14</span></div>
    <div class="tab" style="left:248px">
      <svg width="28" height="28" viewBox="0 0 28 28"><path d="M14 27 C8 18 6 15 6 11 A8 8 0 0 1 22 11 C22 15 20 18 14 27 Z" fill="none" stroke="#5a5a5a" stroke-width="1.5"/><circle cx="14" cy="11" r="3" fill="#5a5a5a"/></svg>Spotted
      <span class="badge" style="left:32px">21</span></div>
    <div class="tab" style="left:326px">
      <svg width="30" height="28" viewBox="0 0 30 28" fill="none" stroke="#5a5a5a" stroke-width="1.5"><path d="M3 14 L27 14 A12 10 0 0 1 3 14 Z"/><path d="M11 25 L19 25"/><path d="M6 4 L24 4 M7 8 L23 8"/><path d="M20 12 L27 2"/></svg>Recipes</div>
  </nav>
</main>
</body>
</html>
```